Brightmoor Partners Branding Revamp

We are a consulting company, looking for a way to display and promote our brand. We have 2 sides to the business- Brightmoor (financial) and Partners (cyber security). The financial side products relate to business necessities: card processing, website design/hosting/maintenance, VoIP phone systems. The cyber security side promotes a bundled package of 4 solutions: network vulnerability scan, dark web scan, anti-ransomeware/malware software, and image-level backups. We want people to understand that partnering with Brightmoor Partners gives them “Trusted Calm Every Day” (tagline). Current badge and logos uploaded.

Target Market(s)

Small businesses

Contact Information for Business Card

Lena Marwick, Vice President, lena@brightmoorpartners.example, 555-806-1937, www.brightmoorpartners.example

Requirements
Nice to have
• I do prefer the darker background for front and back

```html
<!DOCTYPE html>
<html lang="en">
<head>
<meta charset="utf-8">
<title>Brightmoor Partners — Business Card</title>
<link rel="stylesheet" href="https://fonts.googleapis.com/css2?family=Montserrat:wght@500;600;700&family=Nunito+Sans:wght@400;600&display=swap">
<style>
  :root {
    --stage: #1c1c1c;
    --card: #050505;
    --card-edge: #2a2a2a;
    --red: #e8333a;
    --white: #ffffff;
  }
  * { margin: 0; padding: 0; box-sizing: border-box; }
  html, body {
    width: 1200px;
    height: 900px;
    overflow: hidden;
    background: var(--stage);
  }
  .stage {
    position: relative;
    width: 1200px;
    height: 900px;
  }
  .card {
    position: absolute;
    left: 389px;
    width: 424px;
    height: 242px;
    background: var(--card);
    border: 1px solid var(--card-edge);
    border-radius: 12px;
    overflow: hidden;
    font-family: "Montserrat", sans-serif;
    color: var(--white);
  }
  .card--front { top: 174px; }
  .card--back { top: 480px; }

  /* Wordmark */
  .wordmark {
    position: absolute;
    display: flex;
    align-items: center;
    gap: 8px;
    font-family: "Montserrat", sans-serif;
    font-weight: 600;
    color: var(--white);
    text-transform: uppercase;
    white-space: nowrap;
  }
  .wordmark__square {
    flex: none;
    background: var(--red);
  }
  .card--front .wordmark {
    left: 12px;
    top: 62px;
    font-size: 11px;
    letter-spacing: 3px;
  }
  .card--front .wordmark__square { width: 10px; height: 10px; }

  .card--back .wordmark {
    left: 0;
    right: 0;
    top: 118px;
    justify-content: center;
    font-size: 19px;
    letter-spacing: 6px;
  }
  .card--back .wordmark__square { width: 16px; height: 16px; }

  /* Person */
  .person {
    position: absolute;
    left: 0;
    width: 404px;
    top: 116px;
    text-align: center;
  }
  .person__name {
    font-weight: 700;
    font-size: 21px;
    letter-spacing: 0.3px;
    text-transform: uppercase;
  }
  .person__title {
    margin-top: 2px;
    font-family: "Nunito Sans", sans-serif;
    font-weight: 400;
    font-size: 14px;
    color: var(--red);
    text-transform: uppercase;
    letter-spacing: 0.5px;
  }

  .contact {
    position: absolute;
    left: 0;
    right: 0;
    top: 187px;
    text-align: center;
    font-family: "Nunito Sans", sans-serif;
    font-size: 13px;
    text-transform: uppercase;
    white-space: nowrap;
  }
  .contact__divider { color: var(--red); padding: 0 3px; }

  .website-band {
    position: absolute;
    left: 0;
    right: 0;
    bottom: 0;
    height: 24px;
    background: var(--red);
    display: flex;
    align-items: center;
    justify-content: center;
    font-size: 10.5px;
    font-weight: 500;
    letter-spacing: 3.4px;
    text-transform: uppercase;
  }

  .tagline {
    position: absolute;
    left: 0;
    right: 0;
    top: 203px;
    text-align: center;
    color: var(--red);
    font-weight: 500;
    font-size: 15px;
    letter-spacing: 7px;
    text-transform: uppercase;
    white-space: nowrap;
  }
</style>
</head>
<body>
<main class="stage">
  <section class="card card--front" aria-label="Business card front">
    <div class="wordmark"><span class="wordmark__square"></span>Brightmoor Partners</div>
    <div class="person">
      <h1 class="person__name">Lena Marwick</h1>
      <p class="person__title">Vice President</p>
    </div>
    <p class="contact">lena@brightmoorpartners.example<span class="contact__divider">|</span>555-806-1937</p>
    <div class="website-band">www.brightmoorpartners.example</div>
  </section>

  <section class="card card--back" aria-label="Business card back">
    <div class="wordmark"><span class="wordmark__square"></span>Brightmoor Partners</div>
    <p class="tagline">Trusted Calm Every Day</p>
  </section>
</main>
</body>
</html>
```